How likely are people to engage in social distancing? We need a good illustration to show the data!

We surveyed U.S. adults March 20th - 24th, 2020 and asked how likely they were to engage in social distancing (and other COVID-19 related health behaviors). What did the survey find? Basically, most people intend to engage in social distancing behaviors (e.g., avoiding large crowds) and other behaviors that reduce the spread of COVID-19 (e.g., washing hands at least 20 seconds). When most people intend to engage in a behavior, then public health professionals try to leverage that to move more people to act.
Now we need innovative and professional images that attempt to communicate one or all of these findings. The specific findings are nicely summarized in the attached document. For example, 82% of participants intend to engage in social distancing.
What sort of visual are we looking for? Our preference is for an original illustration (or set of illustrations). Our preference is for (creative and powerful illustrations, but we are also open to the creative and well-executed infographics.
We need these images fast . We will award monetary prizes to the 3 best designs. If we like more than that, then we might purchase more (e.g., in past contests, we have purchased as many as 30 designs).
What we will need:
(1) The illustrations must be original and we will need the photoshop and/or illustrator files for all artwork.
(2) You can illustrate all of the findings or just one of them. We need creative approaches that do a lucid job of bringing the data to life. Most people intend to engage in these behaviors. How to communicate that? Corvantists and Halmerites do not differ in their intentions; how to communicate that?
(3) The illustration should say, somewhere: "Based on a survey of 400 U.S. adults conducted March 20 - 24th, 2020."

U.S. Adults

• Original illustrations based on the findings of the survey (see attached document).

```html
<!DOCTYPE html>
<html lang="en">
<head>
<meta charset="utf-8">
<title>How likely are U.S. people to slow the spread of coronavirus?</title>
<link rel="stylesheet" href="https://fonts.googleapis.com/css2?family=Roboto+Condensed:ital,wght@0,400;0,700;1,400&family=Nunito+Sans:ital,wght@0,400;0,800;1,400&display=swap">
<style>
  :root {
    --ink: #111111;
    --muted: #777d80;
    --red: #e0424a;
    --deep-red: #c4282d;
    --slate: #86a5ab;
    --blue: #3e8fe0;
    --track-a: #d8dfe0;
    --track-b: #e4e9ea;
    --rule: #e3e6e7;
    --paper: #ffffff;
  }
  * { margin: 0; padding: 0; box-sizing: border-box; }
  html, body { width: 1200px; height: 2588px; overflow: hidden; background: var(--paper); }
  body { position: relative; font-family: "Nunito Sans", Arial, sans-serif; color: var(--ink); }
  .abs { position: absolute; }

  .title { left: 75px; top: 82px; width: 1100px; font-family: "Roboto Condensed", Arial Narrow, sans-serif; font-weight: 700; font-size: 80px; line-height: 97px; letter-spacing: -0.5px; }
  .subtitle { left: 76px; top: 290px; font-size: 28px; }
  .question { left: 84px; top: 392px; font-size: 31px; font-weight: 800; line-height: 42px; }

  .art { border-radius: 14px; }
  .art--slate { background: linear-gradient(135deg, #9bb6bb, var(--slate)); }
  .art--red { background: linear-gradient(135deg, #e86a70, var(--red)); }
  .art--mixed { background: linear-gradient(135deg, var(--red), var(--slate)); }

  .stat-value { font-family: "Roboto Condensed", Arial Narrow, sans-serif; font-weight: 700; font-size: 66px; line-height: 66px; letter-spacing: -1px; }
  .stat-label { font-size: 25px; line-height: 33px; color: var(--muted); }

  .section-head { left: 75px; top: 1400px; font-size: 31px; font-weight: 800; }
  .section-sub { left: 78px; top: 1444px; font-size: 28px; }

  .chart { left: 0; top: 0; }
  .row-label { font-family: "Nunito Sans", Arial, sans-serif; font-size: 25px; fill: var(--muted); }
  .pct { font-family: "Roboto Condensed", Arial Narrow, sans-serif; font-weight: 700; font-size: 31px; fill: var(--ink); }
  .party { font-family: "Nunito Sans", Arial, sans-serif; font-weight: 800; font-size: 25px; }

  .takeaway-head { left: 80px; top: 2180px; font-size: 31px; font-weight: 800; }
  .takeaway { left: 383px; top: 2258px; width: 720px; font-family: "Roboto Condensed", Arial Narrow, sans-serif; font-weight: 700; font-size: 45px; line-height: 54px; color: var(--deep-red); }
  .source { right: 41px; top: 2543px; font-style: italic; font-size: 21px; color: var(--muted); }
</style>
</head>
<body>

<h1 class="abs title">How likely are U.S. people to slow the spread of coronavirus?</h1>
<p class="abs subtitle">Percent of Americans intending to engage in COVID-19 health behaviors</p>
<h2 class="abs question">We would like to know how likely it is that you will perform<br>these behaviors to slow the spread of coronavirus?</h2>

<!-- Behaviour stats, left column -->
<div class="abs art art--mixed" style="left:93px;top:528px;width:172px;height:176px" role="img" aria-label="Illustration of connected people standing on a globe"></div>
<div class="abs stat-value" style="left:305px;top:523px">82%</div>
<div class="abs stat-label" style="left:306px;top:598px">intend to engage in<br>social distancing</div>

<div class="abs art art--red" style="left:95px;top:752px;width:170px;height:162px" role="img" aria-label="Illustration of a person working at a desk inside a house"></div>
<div class="abs stat-value" style="left:305px;top:743px">63%</div>
<div class="abs stat-label" style="left:306px;top:813px">intend to work<br>from home</div>

<div class="abs art art--slate" style="left:103px;top:958px;width:152px;height:168px" role="img" aria-label="Illustration of a crossed-out group gathering"></div>
<div class="abs stat-value" style="left:305px;top:952px">85%</div>
<div class="abs stat-label" style="left:306px;top:1020px">intend to avoid<br>large gatherings</div>

<div class="abs art art--slate" style="left:93px;top:1176px;width:162px;height:140px" role="img" aria-label="Illustration of three people with cancelled speech bubbles"></div>
<div class="abs stat-value" style="left:305px;top:1168px">81%</div>
<div class="abs stat-label" style="left:306px;top:1236px">intend to cancel<br>social activities</div>

<!-- Behaviour stats, right column -->
<div class="abs art art--slate" style="left:626px;top:528px;width:176px;height:180px" role="img" aria-label="Illustration of two people separated by a distance arrow"></div>
<div class="abs stat-value" style="left:830px;top:523px">85%</div>
<div class="abs stat-label" style="left:831px;top:594px">intend to put distance<br>between yourself and<br>other people</div>

<div class="abs art art--mixed" style="left:623px;top:738px;width:180px;height:184px" role="img" aria-label="Illustration of hands being washed under a tap"></div>
<div class="abs stat-value" style="left:830px;top:756px">87%</div>
<div class="abs stat-label" style="left:831px;top:827px">intend to wash hands<br>at least 20 seconds</div>

<div class="abs art art--mixed" style="left:626px;top:982px;width:176px;height:130px" role="img" aria-label="Illustration of a sanitizer bottle and an open hand"></div>
<div class="abs stat-value" style="left:840px;top:963px">85%</div>
<div class="abs stat-label" style="left:841px;top:1027px">intend to use<br>hand sanitizer</div>

<div class="abs art art--mixed" style="left:630px;top:1188px;width:178px;height:160px" role="img" aria-label="Illustration of eyes, nose and mouth with a raised hand"></div>
<div class="abs stat-value" style="left:840px;top:1139px">81%</div>
<div class="abs stat-label" style="left:841px;top:1212px">intend to avoid<br>touching your eyes,<br>nose, and mouth</div>

<!-- Party comparison -->
<h2 class="abs section-head">Comparing Corvantists and Halmerites</h2>
<p class="abs section-sub">March 20th - 24th, 2020 Survey</p>

<svg class="abs chart" width="1200" height="2588" viewBox="0 0 1200 2588" aria-label="Comparison chart of intended behaviours by party">
  <text class="party" x="650" y="1515" text-anchor="middle" fill="var(--red)">Corvantists</text>
  <text class="party" x="965" y="1516" text-anchor="middle" fill="var(--blue)">Halmerites</text>

  <g stroke="var(--rule)" stroke-width="1.5">
    <line x1="81" y1="1606" x2="1139" y2="1606"/>
    <line x1="81" y1="1667" x2="1139" y2="1667"/>
    <line x1="81" y1="1731" x2="1139" y2="1731"/>
    <line x1="81" y1="1794" x2="1139" y2="1794"/>
    <line x1="81" y1="1889" x2="1139" y2="1889"/>
    <line x1="81" y1="1978" x2="1139" y2="1978"/>
    <line x1="81" y1="2037" x2="1139" y2="2037"/>
  </g>

  <!-- row: label / track / dots / values -->
  <g>
    <text class="row-label" x="81" y="1584">Engage in social distancing</text>
    <rect x="563" y="1566" width="249" height="18" fill="var(--track-a)"/><rect x="812" y="1566" width="248" height="18" fill="var(--track-b)"/>
    <circle cx="563" cy="1575" r="10" fill="var(--red)"/><circle cx="1060" cy="1575" r="10" fill="var(--blue)"/>
    <text class="pct" x="549" y="1586" text-anchor="end">82%</text><text class="pct" x="1074" y="1586">81%</text>
  </g>
  <g>
    <text class="row-label" x="81" y="1646">Work from home</text>
    <rect x="629" y="1628" width="183" height="18" fill="var(--track-a)"/><rect x="812" y="1628" width="199" height="18" fill="var(--track-b)"/>
    <circle cx="629" cy="1637" r="10" fill="var(--red)"/><circle cx="1011" cy="1637" r="10" fill="var(--blue)"/>
    <text class="pct" x="615" y="1648" text-anchor="end">60%</text><text class="pct" x="1025" y="1648">65%</text>
  </g>
  <g>
    <text class="row-label" x="81" y="1707">Avoid large gatherings</text>
    <rect x="554" y="1689" width="258" height="18" fill="var(--track-a)"/><rect x="812" y="1689" width="257" height="18" fill="var(--track-b)"/>
    <circle cx="554" cy="1698" r="10" fill="var(--red)"/><circle cx="1069" cy="1698" r="10" fill="var(--blue)"/>
    <text class="pct" x="540" y="1709" text-anchor="end">85%</text><text class="pct" x="1083" y="1709">84%</text>
  </g>
  <g>
    <text class="row-label" x="81" y="1771">Cancel social activities</text>
    <rect x="563" y="1753" width="249" height="18" fill="var(--track-a)"/><rect x="812" y="1753" width="246" height="18" fill="var(--track-b)"/>
    <circle cx="563" cy="1762" r="10" fill="var(--red)"/><circle cx="1058" cy="1762" r="10" fill="var(--blue)"/>
    <text class="pct" x="549" y="1773" text-anchor="end">82%</text><text class="pct" x="1072" y="1773">80%</text>
  </g>
  <g>
    <text class="row-label" x="81" y="1832">Put distance between yourself</text>
    <text class="row-label" x="81" y="1865">and other people</text>
    <rect x="557" y="1830" width="255" height="18" fill="var(--track-a)"/><rect x="812" y="1830" width="265" height="18" fill="var(--track-b)"/>
    <circle cx="557" cy="1839" r="10" fill="var(--red)"/><circle cx="1077" cy="1839" r="10" fill="var(--blue)"/>
    <text class="pct" x="543" y="1850" text-anchor="end">84%</text><text class="pct" x="1091" y="1850">87%</text>
  </g>
  <g>
    <text class="row-label" x="81" y="1927">Wash hands at least 20</text>
    <text class="row-label" x="81" y="1960">seconds</text>
    <rect x="548" y="1912" width="264" height="18" fill="var(--track-a)"/><rect x="812" y="1912" width="271" height="18" fill="var(--track-b)"/>
    <circle cx="548" cy="1921" r="10" fill="var(--red)"/><circle cx="1083" cy="1921" r="10" fill="var(--blue)"/>
    <text class="pct" x="534" y="1932" text-anchor="end">87%</text><text class="pct" x="1097" y="1932">88%</text>
  </g>
  <g>
    <text class="row-label" x="81" y="2018">Use hand sanitizer</text>
    <rect x="548" y="2000" width="264" height="18" fill="var(--track-a)"/><rect x="812" y="2000" width="257" height="18" fill="var(--track-b)"/>
    <circle cx="548" cy="2009" r="10" fill="var(--red)"/><circle cx="1069" cy="2009" r="10" fill="var(--blue)"/>
    <text class="pct" x="534" y="2020" text-anchor="end">87%</text><text class="pct" x="1083" y="2020">84%</text>
  </g>
  <g>
    <text class="row-label" x="81" y="2073">Avoid touching your eyes, nose,</text>
    <text class="row-label" x="81" y="2106">and mouth</text>
    <rect x="567" y="2066" width="245" height="18" fill="var(--track-a)"/><rect x="812" y="2066" width="251" height="18" fill="var(--track-b)"/>
    <circle cx="567" cy="2075" r="10" fill="var(--red)"/><circle cx="1063" cy="2075" r="10" fill="var(--blue)"/>
    <text class="pct" x="553" y="2086" text-anchor="end">80%</text><text class="pct" x="1077" y="2086">82%</text>
  </g>
</svg>

<!-- Takeaway -->
<h2 class="abs takeaway-head">What does this data say?</h2>
<div class="abs art art--slate" style="left:98px;top:2282px;width:250px;height:232px" role="img" aria-label="Illustration of a clipboard with a magnifying glass"></div>
<p class="abs takeaway">It says that most people both Corvantists and Halmerites are intend to slow the spread of coronavirus by engaging these behaviors.</p>

<p class="abs source">Based on a survey of 400 U.S. adults conducted March 20 - 24th, 2020</p>

</body>
</html>
```